Flyer für Immobilienmakler
Top Arbeit vom Designer. Er hat alle Idee schnell und professionell umgesetzt und das Ergebnis kann sich sehen lassen. Herzlichen Dank für die großartige Arbeit. Immer wieder gerne.
Zielgruppe
Immobilienmakler, Zielgruppe sind Menschen die uns weiterempfehlen um ihre Immobilie zu verkaufen
Aufgabenstellung
Ein Flyer DIN lang quer, Vorder und Rückseite, Es geht um eine Tippgeberprovision welche Menschen bekommen die uns einen Verkaufskunden bringen, diese erhalten 10 %- genaue Texte und Hinweise werde ich einbringen, Unser Slogan: 'Unsere Erfahrung für Ihren Vorteil'
Nachtrag. Bei dem Flyer 'Vom Berg Immobilien' finde ich die blauen Banner/ Streifen gut- ist aber kein Muss. Update: Es war als Inspiration von meiner Seite gedacht. Auf keinen Fall darf es genauso aussehen!!
Meine jetzige Webseite ist auch gut um die Farben zu erkennen, jedoch nicht unbedingt das Design, da ich gerade eine neue Webseite erstellen lasse

```html
<!DOCTYPE html>
<html lang="de">
<head>
<meta charset="utf-8">
<title>Tippgeberprovision – NOVARA Immobilien</title>
<link rel="stylesheet" href="https://fonts.googleapis.com/css2?family=Bebas+Neue&family=Roboto:wght@400;500&family=Roboto+Condensed:wght@700&display=swap">
<style>
  :root {
    --navy-deep: #0c1f3a;
    --navy-mid: #1a3557;
    --navy-text: #1f2d4a;
    --ice: #d3e8f7;
    --band: #d5eaf8;
    --orange: #f0a000;
    --white: #ffffff;
    --grey: #6b7480;
  }
  * { margin: 0; padding: 0; box-sizing: border-box; }
  html, body { width: 1200px; height: 600px; overflow: hidden; background: var(--navy-deep); }
  .flyer {
    position: relative;
    width: 1200px;
    height: 600px;
    overflow: hidden;
    background: radial-gradient(ellipse at 30% 40%, #1d3a5e 0%, var(--navy-deep) 70%);
    font-family: "Roboto", sans-serif;
  }
  .hero-photo {
    position: absolute;
    left: 560px; top: 0;
    width: 640px; height: 600px;
    background:
      radial-gradient(ellipse at 42% 48%, #c99a78 0%, rgba(201,154,120,0.55) 14%, rgba(26,53,87,0) 34%),
      linear-gradient(90deg, rgba(12,31,58,0) 0%, var(--navy-mid) 45%, #15263f 100%);
  }
  .headline {
    position: absolute;
    left: 60px; top: 48px;
    font-family: "Bebas Neue", sans-serif;
    font-weight: 400;
    font-size: 60px;
    letter-spacing: 1px;
    color: var(--ice);
    line-height: 1;
    white-space: nowrap;
  }
  .rate {
    position: absolute;
    left: 32px; top: 122px;
    font-family: "Bebas Neue", sans-serif;
    font-size: 420px;
    letter-spacing: -6px;
    line-height: 1;
    color: var(--ice);
    transform: scaleX(0.9);
    transform-origin: left top;
  }
  .rate-percent {
    position: absolute;
    left: 326px; top: 117px;
    font-family: "Roboto Condensed", sans-serif;
    font-weight: 700;
    font-size: 250px;
    line-height: 1;
    color: var(--ice);
    transform: scaleX(1.1);
    transform-origin: left top;
  }
  .rate-note {
    position: absolute;
    left: 350px; top: 352px;
    font-size: 19px;
    line-height: 25.5px;
    color: var(--ice);
  }
  .slogan-badge {
    position: absolute;
    left: 967px; top: 75px;
    width: 182px; height: 182px;
    border-radius: 50%;
    background: var(--orange);
    border: 4px solid var(--white);
    display: flex; align-items: center; justify-content: center;
    text-align: center;
    font-family: "Roboto Condensed", sans-serif;
    font-weight: 700;
    font-size: 24px;
    line-height: 1.12;
    text-transform: uppercase;
    color: var(--white);
  }
  .footer-band { position: absolute; left: 0; bottom: 0; width: 1200px; height: 130px; }
  .contact {
    position: absolute;
    top: 558px;
    display: flex; align-items: center; gap: 12px;
    font-size: 22px;
    color: var(--navy-text);
  }
  .contact-mail { left: 52px; }
  .contact-phone { left: 402px; }
  .contact svg { fill: var(--navy-text); }
  .brand {
    position: absolute;
    right: 36px; top: 494px;
    text-align: right;
    color: var(--navy-text);
  }
  .brand-name {
    font-family: "Roboto", sans-serif;
    font-weight: 500;
    font-size: 58px;
    letter-spacing: 5px;
    line-height: 1;
  }
  .brand-sub { font-size: 17px; color: var(--grey); margin-top: 6px; }
</style>
</head>
<body>
<div class="flyer">
  <div class="hero-photo" role="img" aria-label="Geschäftsmann im Anzug hält ein Hausmodell auf der Hand"></div>

  <h1 class="headline">Unser Tipp für alle Tippgeber</h1>
  <div class="rate">10</div>
  <div class="rate-percent">%</div>
  <p class="rate-note">Tippgeberprovision<br>für jeden der uns<br>einen Verkaufskunden<br>vermittelt.</p>

  <div class="slogan-badge">Unsere<br>Erfahrung<br>für Ihren<br>Vorteil</div>

  <svg class="footer-band" viewBox="0 0 1200 130" preserveAspectRatio="none" aria-hidden="true">
    <path d="M0 72 H790 C860 72 870 0 960 0 H1200 V130 H0 Z" fill="var(--band)"/>
  </svg>

  <div class="contact contact-mail">
    <svg width="32" height="22" viewBox="0 0 32 22" aria-hidden="true">
      <path d="M1 1h30v20H1z M3 3v1l13 9 13-9V3z M3 6.5V19h26V6.5L16 15.5z" fill-rule="evenodd"/>
    </svg>
    <span>kontakt@novara.immo</span>
  </div>
  <div class="contact contact-phone">
    <svg width="22" height="24" viewBox="0 0 24 24" aria-hidden="true">
      <path d="M6.6 10.8c1.4 2.8 3.8 5.1 6.6 6.6l2.2-2.2c.3-.3.7-.4 1-.2 1.1.4 2.3.6 3.6.6.6 0 1 .4 1 1V20c0 .6-.4 1-1 1C10.6 21 3 13.4 3 4c0-.6.4-1 1-1h3.5c.6 0 1 .4 1 1 0 1.3.2 2.5.6 3.6.1.3 0 .7-.2 1z"/>
    </svg>
    <span>+49 (0)6251 4701285</span>
  </div>

  <div class="brand">
    <div class="brand-name">NOVARA</div>
    <div class="brand-sub">Immobilien</div>
  </div>
</div>
</body>
</html>
```